Looking for a high-end business card design for a construction company

We are looking to update our business card design. We are a post-frame construction company that builds custom buildings, commercial spaces, homes, and anything else. We have multiple people working here so we would need something we can easily customize the information for the specific person. We need a name, website, cell phone, office phone as well as social icons. Our colors are black, white, and grey/silver so I would love a black background or something that is more striking than just a traditional white business card. Looking for something that is very professional with a high-end look/feel. I have attached our logos, they can be silver, white, grey, or black.
Industry/Entity Type
Construction
Contact Information for Business Card
Business logo, Name, Cell phone, Office phone, website, social Icons
Colors
Designer to choose only greyscale colors for use in the design.
Look and feel

```html
<!DOCTYPE html>
<html lang="en">
<head>
<meta charset="utf-8">
<title>Ridgeline Builders, Co. — Business Card</title>
<link rel="stylesheet" href="https://fonts.googleapis.com/css2?family=Arimo:wght@400;700&display=swap">
<style>
  :root {
    --stage: #a9a9a9;
    --card: #1f1f1f;
    --ink: #ffffff;
    --silver: #d4d4d4;
    --muted: #c9c9c9;
    --rule: #8a8a8a;
  }
  * { margin: 0; padding: 0; box-sizing: border-box; }
  html, body { width: 1200px; height: 788px; overflow: hidden; }
  body {
    background: var(--stage);
    font-family: "Arimo", Arial, sans-serif;
    color: var(--ink);
    position: relative;
  }
  .card {
    position: absolute;
    top: 234px;
    width: 560px;
    height: 320px;
    background: var(--card);
    border-radius: 22px;
  }
  .card--front { left: 30px; }
  .card--back { left: 610px; }

  .brand { position: absolute; display: flex; align-items: center; color: var(--silver); font-weight: 700; text-transform: uppercase; }
  .brand__dot { border-radius: 50%; background: var(--silver); flex: none; }
  .brand__name { line-height: 1.05; letter-spacing: 2px; }

  .card--front .brand { left: 34px; top: 128px; gap: 12px; }
  .card--front .brand__dot { width: 30px; height: 30px; }
  .card--front .brand__name { font-size: 19px; }

  .divider { position: absolute; left: 262px; top: 52px; width: 1px; height: 186px; background: var(--rule); }

  .details { position: absolute; left: 288px; top: 50px; }
  .details__name { font-size: 23px; font-weight: 700; }
  .details__title { font-size: 13px; color: var(--muted); margin-top: 3px; }
  .details__address { font-size: 13px; color: var(--muted); margin-top: 14px; line-height: 1.35; }
  .contact { list-style: none; margin-top: 12px; }
  .contact li { display: flex; align-items: center; gap: 7px; font-size: 13px; color: var(--muted); line-height: 1.6; }
  .contact svg { width: 11px; height: 11px; flex: none; }

  .social { position: absolute; left: 34px; bottom: 32px; display: flex; align-items: center; gap: 5px; font-size: 14px; color: var(--ink); }
  .social__dot { width: 14px; height: 14px; border-radius: 50%; background: var(--ink); }
  .social__handle { margin-left: 6px; }

  .card--back .brand { left: 0; right: 0; top: 110px; justify-content: center; gap: 18px; }
  .card--back .brand__dot { width: 54px; height: 54px; }
  .card--back .brand__name { font-size: 36px; letter-spacing: 3px; }
</style>
</head>
<body>
  <section class="card card--front">
    <div class="brand">
      <span class="brand__dot"></span>
      <span class="brand__name">Ridgeline<br>Builders, Co.</span>
    </div>
    <div class="divider"></div>
    <div class="details">
      <h1 class="details__name">Dalia Westbrook</h1>
      <p class="details__title">Director of Education</p>
      <p class="details__address">1820 North Alder Avenue<br>Lakewood, CO 80214</p>
      <ul class="contact">
        <li>
          <svg viewBox="0 0 12 12" aria-hidden="true"><circle cx="6" cy="6" r="6" fill="#c9c9c9"/><path d="M4 3.2l1 .1.4 1.5-.7.6a4 4 0 0 0 1.9 1.9l.6-.7 1.5.4.1 1c-3 .6-5.4-1.8-4.8-4.8z" fill="#1f1f1f"/></svg>
          555.214.0193
        </li>
        <li>
          <svg viewBox="0 0 12 12" aria-hidden="true"><rect x="0.5" y="2.5" width="11" height="7" fill="#c9c9c9"/><path d="M0.5 2.5L6 6.6l5.5-4.1" stroke="#1f1f1f" fill="none"/></svg>
          info@ridgelinebuildersco.com
        </li>
        <li>
          <svg viewBox="0 0 12 12" aria-hidden="true"><circle cx="6" cy="6" r="5.5" fill="#c9c9c9"/><path d="M0.5 6h11M6 .5c-2.5 3-2.5 8 0 11M6 .5c2.5 3 2.5 8 0 11" stroke="#1f1f1f" stroke-width=".8" fill="none"/></svg>
          www.ridgelinebuildersco.com
        </li>
      </ul>
    </div>
    <div class="social">
      <span class="social__dot"></span>
      <span class="social__dot"></span>
      <span class="social__dot"></span>
      <span class="social__dot"></span>
      <span class="social__handle">@ridgelinebuildersco</span>
    </div>
  </section>

  <section class="card card--back">
    <div class="brand">
      <span class="brand__dot"></span>
      <span class="brand__name">Ridgeline<br>Builders, Co.</span>
    </div>
  </section>
</body>
</html>
```